Dental promotion

We are a family dental office that provides 99% of the dental service for the entire family, including IV sedation, wisdom teeth extraction, implant, Clearvanta, root canal, teeth whiting et cl. We currently have promotion for Clearvanta, implant and new patients who don’t have insurance. 1500 off Clearvanta, 2000 off for implant, 98 dollars for new patient that cover exam, x-ray, and regular cleaning. We also offer financing option.
More information please check our website
https://www.brookhollowfamilydentistry.example/

```html
<!DOCTYPE html>
<html lang="en">
<head>
<meta charset="utf-8">
<title>Brookhollow Family Dentistry – Postcard</title>
<link href="https://fonts.googleapis.com/css2?family=Ubuntu:wght@400;500;700&family=Open+Sans:wght@400;600&family=Roboto+Condensed:wght@400;700&family=Oswald:wght@400;500&display=swap" rel="stylesheet">
<style>
  :root{
    --green:#5a9e1e;
    --blue:#2e3192;
    --white:#ffffff;
    --ink:#333333;
    --table:#b3b3b3;
    --rule:#c9c9c9;
    --offer-accent:#7cc242;
  }
  *{margin:0;padding:0;box-sizing:border-box}
  html,body{width:1200px;height:904px;overflow:hidden}
  body{background:var(--table);position:relative;font-family:"Open Sans",sans-serif;color:var(--ink)}
  .card{position:absolute;width:542px;height:361px;background:var(--white);overflow:hidden;box-shadow:0 4px 12px rgba(0,0,0,.25)}
  .card--front{left:219px;top:73px}
  .card--back{left:475px;top:469px}
  .card-art{position:absolute;inset:0;width:542px;height:361px}
  .abs{position:absolute}

  .brand{display:flex;align-items:center;gap:7px}
  .brand-dot{border-radius:50%;border:3px solid var(--blue);flex:none}
  .brand-name{font-family:"Ubuntu",sans-serif;font-weight:500;color:var(--blue);line-height:1.1;text-transform:uppercase;white-space:nowrap}
  .card--front .brand{left:24px;top:42px}
  .card--front .brand-dot{width:40px;height:40px;border-width:4px}
  .card--front .brand-name{font-size:16px;letter-spacing:1.2px}
  .card--back .brand{left:302px;top:24px;gap:5px}
  .card--back .brand-dot{width:25px;height:25px;border-width:3px}
  .card--back .brand-name{font-size:9.6px;letter-spacing:.5px}

  .headline{left:23px;top:111px;font-family:"Ubuntu",sans-serif;font-weight:700;font-size:24px;line-height:30px;color:var(--white)}
  .section-title{font-family:"Ubuntu",sans-serif;font-weight:700;color:var(--green);text-transform:uppercase}
  .section-title .accent{color:var(--blue)}
  .mission-title{left:23px;top:188px;font-size:15px}
  .mission-text{left:23px;top:208px;font-size:8.3px;line-height:12.1px}
  .mission-text span{display:block;white-space:nowrap;text-align:justify;text-align-last:justify}
  .mission-text .last{text-align-last:left}

  .contact{font-family:"Ubuntu",sans-serif;color:var(--white);font-size:8.3px;display:flex;align-items:center;gap:3px;white-space:nowrap}
  .contact svg{width:8.5px;height:8.5px;flex:none}
  .contact strong{font-weight:700}
  .front-contact-1{left:23px;top:326px}
  .front-contact-2{left:23px;top:341px}
  .back-contact{left:23px;top:342px}

  .services-title{left:23px;top:20px;font-size:12px}
  .services{font-family:"Ubuntu",sans-serif;font-size:10.4px;line-height:15px;color:#222;list-style:none}
  .services li{display:flex;gap:5px;align-items:flex-start}
  .services li svg{width:8px;height:8px;margin-top:3.5px;flex:none}
  .services--a{left:23px;top:35px;width:122px}
  .services--b{left:150px;top:35px;width:110px}

  .promo-intro{left:23px;top:135px;font-family:"Ubuntu",sans-serif;font-weight:500;font-size:10px;line-height:12.5px;color:var(--white)}
  .offer{top:166px;height:24px;background:var(--blue);border-radius:2px;font-family:"Oswald",sans-serif;font-size:11px;color:var(--white);display:flex;align-items:center;justify-content:center;letter-spacing:-.3px;white-space:nowrap}
  .offer span{color:var(--offer-accent);margin-left:3px}
  .offer--aligner{left:23px;width:122px}
  .offer--implant{left:152px;width:119px}
  .price{left:22px;top:193px;font-family:"Oswald",sans-serif;font-weight:500;font-size:24px;color:var(--white);line-height:28px;letter-spacing:-1px}
  .price-note{left:61px;top:196px;font-size:9.4px;line-height:12.5px;color:var(--white);white-space:nowrap}

  .doctor-title{left:22px;top:234px;font-size:12px;color:var(--blue)}
  .doctor-bio{left:23px;top:250px;width:222px;font-family:"Roboto Condensed",sans-serif;font-size:9.6px;line-height:12.1px;text-align:justify}

  .return-address{left:303px;top:74px;font-family:"Ubuntu",sans-serif;font-size:9.4px;line-height:12px;color:#222}
  .stamp-box{left:461px;top:22px;width:62px;height:57px;border:2px solid var(--rule)}
  .address-line{height:1.5px;background:var(--rule);right:20px}
  .address-line--1{top:145px;left:337px}
  .address-line--2{top:186px;left:354px}
  .address-line--3{top:227px;left:367px}
</style>
</head>
<body>

<section class="card card--front" aria-label="Postcard front">
  <svg class="card-art" viewBox="0 0 542 361" aria-hidden="true">
    <defs>
      <linearGradient id="clinicTone" x1="0" y1="0" x2="1" y2="1">
        <stop offset="0" stop-color="#d9cfc8"/>
        <stop offset=".45" stop-color="#e9e3df"/>
        <stop offset=".8" stop-color="#c99a84"/>
        <stop offset="1" stop-color="#8fd0e6"/>
      </linearGradient>
      <linearGradient id="smileTone" x1="0" y1="0" x2="1" y2="1">
        <stop offset="0" stop-color="#b9d8e4"/>
        <stop offset="1" stop-color="#e3b8a6"/>
      </linearGradient>
    </defs>
    <path d="M300 0 C268 45 262 130 300 235 L322 361 L542 361 L542 0 Z" fill="url(#clinicTone)"/>
    <path d="M291 0 C258 45 251 135 292 240" fill="none" stroke="var(--green)" stroke-width="3.5"/>
    <path d="M284 20 C262 70 262 160 312 262" fill="none" stroke="var(--blue)" stroke-width="3.5"/>
    <polygon points="0,105 247,105 266,181 0,181" fill="var(--green)"/>
    <polygon points="0,318 287,318 268,361 0,361" fill="var(--blue)"/>
    <polygon points="276,361 296,318 302,318 282,361" fill="var(--white)"/>
    <polygon points="286,361 304,322 309,322 292,361" fill="var(--blue)"/>
    <circle cx="293" cy="283" r="53" fill="var(--white)"/>
    <circle cx="293" cy="283" r="50" fill="url(#smileTone)" stroke="var(--green)" stroke-width="4"/>
  </svg>
  <div class="abs" role="img" aria-label="Photo of a dentist examining a patient in the dental chair" style="left:300px;top:0;width:242px;height:361px"></div>
  <div class="abs" role="img" aria-label="Close-up photo of a patient's smile during a check-up" style="left:243px;top:233px;width:100px;height:100px;border-radius:50%"></div>

  <div class="abs brand">
    <span class="brand-dot"></span>
    <span class="brand-name">Brookhollow<br>Family Dentistry</span>
  </div>

  <h1 class="abs headline">YOUR TOP RATED<br>RALEIGH DENTIST.</h1>

  <h2 class="abs section-title mission-title">Our <span class="accent">Mission</span></h2>
  <p class="abs mission-text">
    <span style="width:232px">Our Mission is to provide superior family &amp; cosmetic</span>
    <span style="width:222px">dental care in a friendly, comfortable, modern, and</span>
    <span style="width:214px">safe environment. We strive to meet the unique</span>
    <span style="width:207px">needs of each patient with empathy, patience,</span>
    <span style="width:202px">honesty, and fairness. It is our hope that we</span>
    <span style="width:199px">earn your trust and confidence and in return,</span>
    <span style="width:199px">you will not hesitate to refer us your family,</span>
    <span class="last" style="width:199px">friends, and co-workers.</span>
  </p>

  <div class="abs contact front-contact-1">
    <svg viewBox="0 0 10 10"><circle cx="5" cy="5" r="5" fill="var(--green)"/><path d="M5 2.2a1.8 1.8 0 0 0-1.8 1.8c0 1.4 1.8 3.6 1.8 3.6s1.8-2.2 1.8-3.6A1.8 1.8 0 0 0 5 2.2z" fill="var(--white)"/></svg>
    4270 Maplecrest Drive, Suite #210 Raleigh, NC 27615
  </div>
  <div class="abs contact front-contact-2">
    <svg viewBox="0 0 10 10"><circle cx="5" cy="5" r="5" fill="var(--green)"/><path d="M3.3 2.5l1 1-.5.7c.4.8 1 1.4 1.9 1.9l.7-.5 1 1-.7.9C4.8 7.2 2.8 5.2 2.5 3.2z" fill="var(--white)"/></svg>
    <strong>919-555-0148</strong>&nbsp;
    <svg viewBox="0 0 10 10"><circle cx="5" cy="5" r="5" fill="var(--green)"/><circle cx="5" cy="5" r="3" fill="none" stroke="var(--white)" stroke-width=".7"/><path d="M2 5h6M5 2c-1.4 1.6-1.4 4.4 0 6M5 2c1.4 1.6 1.4 4.4 0 6" fill="none" stroke="var(--white)" stroke-width=".6"/></svg>
    www.brookhollowfamilydentistry.example
  </div>
</section>

<section class="card card--back" aria-label="Postcard back">
  <svg class="card-art" viewBox="0 0 542 361" aria-hidden="true">
    <polygon points="0,128 272,128 313,228 0,228" fill="var(--green)"/>
    <path d="M305 0 C278 35 270 100 290 165 C300 200 310 225 318 250" fill="none" stroke="var(--green)" stroke-width="3.5"/>
    <path d="M298 14 C273 60 270 130 300 200 C306 215 312 228 316 240" fill="none" stroke="var(--blue)" stroke-width="3.5"/>
    <polygon points="0,334 298,334 286,361 0,361" fill="var(--blue)"/>
    <polygon points="292,361 304,336 309,336 298,361" fill="var(--blue)"/>
    <circle cx="304" cy="290" r="54" fill="var(--white)"/>
    <circle cx="304" cy="290" r="51" fill="#c7d3d6" stroke="var(--green)" stroke-width="4"/>
  </svg>
  <div class="abs" role="img" aria-label="Portrait photo of the dentist" style="left:253px;top:239px;width:102px;height:102px;border-radius:50%"></div>

  <h2 class="abs section-title services-title">Our Services:</h2>
  <ul class="abs services services--a">
    <li><svg viewBox="0 0 10 10"><circle cx="5" cy="5" r="5" fill="var(--blue)"/><path d="M2.8 5.1l1.5 1.5 3-3" fill="none" stroke="var(--white)" stroke-width="1.3"/></svg>Short-Term Braces</li>
    <li><svg viewBox="0 0 10 10"><circle cx="5" cy="5" r="5" fill="var(--blue)"/><path d="M2.8 5.1l1.5 1.5 3-3" fill="none" stroke="var(--white)" stroke-width="1.3"/></svg>Cosmetic Dentistry</li>
    <li><svg viewBox="0 0 10 10"><circle cx="5" cy="5" r="5" fill="var(--blue)"/><path d="M2.8 5.1l1.5 1.5 3-3" fill="none" stroke="var(--white)" stroke-width="1.3"/></svg>Root Canal Therapy</li>
    <li><svg viewBox="0 0 10 10"><circle cx="5" cy="5" r="5" fill="var(--blue)"/><path d="M2.8 5.1l1.5 1.5 3-3" fill="none" stroke="var(--white)" stroke-width="1.3"/></svg>Teeth Whitening</li>
    <li><svg viewBox="0 0 10 10"><circle cx="5" cy="5" r="5" fill="var(--blue)"/><path d="M2.8 5.1l1.5 1.5 3-3" fill="none" stroke="var(--white)" stroke-width="1.3"/></svg><span style="line-height:12.5px;margin-top:1px">Implant-Supported Dentures</span></li>
  </ul>
  <ul class="abs services services--b">
    <li><svg viewBox="0 0 10 10"><circle cx="5" cy="5" r="5" fill="var(--blue)"/><path d="M2.8 5.1l1.5 1.5 3-3" fill="none" stroke="var(--white)" stroke-width="1.3"/></svg>Veneers</li>
    <li><svg viewBox="0 0 10 10"><circle cx="5" cy="5" r="5" fill="var(--blue)"/><path d="M2.8 5.1l1.5 1.5 3-3" fill="none" stroke="var(--white)" stroke-width="1.3"/></svg>Dental Crowns</li>
    <li><svg viewBox="0 0 10 10"><circle cx="5" cy="5" r="5" fill="var(--blue)"/><path d="M2.8 5.1l1.5 1.5 3-3" fill="none" stroke="var(--white)" stroke-width="1.3"/></svg>Dental Fillings</li>
    <li><svg viewBox="0 0 10 10"><circle cx="5" cy="5" r="5" fill="var(--blue)"/><path d="M2.8 5.1l1.5 1.5 3-3" fill="none" stroke="var(--white)" stroke-width="1.3"/></svg>Dental Bridges</li>
    <li><svg viewBox="0 0 10 10"><circle cx="5" cy="5" r="5" fill="var(--blue)"/><path d="M2.8 5.1l1.5 1.5 3-3" fill="none" stroke="var(--white)" stroke-width="1.3"/></svg>Gum Surgery</li>
  </ul>

  <p class="abs promo-intro">We currently have promotion for Clearvanta,<br>implant &amp; new patients who don’t have insurance.</p>
  <div class="abs offer offer--aligner">1500 OFF<span>FOR CLEARVANTA</span></div>
  <div class="abs offer offer--implant">2000 OFF<span>FOR IMPLANT</span></div>
  <div class="abs price">$98</div>
  <p class="abs price-note">For new patient that cover exam, x-ray, and<br>regular cleaning. We also offer financing option.</p>

  <h2 class="abs section-title doctor-title">Dr. Hale</h2>
  <p class="abs doctor-bio">Dr. Hale keeps up with the latest advances in dentistry by attending continuing education courses &amp; takes pride in offering state-of-the-art quality dental care with a gentle touch. When Dr. Hale is not creating life-changing smiles at his practice, he enjoys spending time with his wife &amp; two sons engaging in outdoor activities.</p>

  <div class="abs contact back-contact">
    <svg viewBox="0 0 10 10"><circle cx="5" cy="5" r="5" fill="var(--green)"/><path d="M3.3 2.5l1 1-.5.7c.4.8 1 1.4 1.9 1.9l.7-.5 1 1-.7.9C4.8 7.2 2.8 5.2 2.5 3.2z" fill="var(--white)"/></svg>
    <strong>919-555-0148</strong>&nbsp;
    <svg viewBox="0 0 10 10"><circle cx="5" cy="5" r="5" fill="var(--green)"/><circle cx="5" cy="5" r="3" fill="none" stroke="var(--white)" stroke-width=".7"/><path d="M2 5h6M5 2c-1.4 1.6-1.4 4.4 0 6M5 2c1.4 1.6 1.4 4.4 0 6" fill="none" stroke="var(--white)" stroke-width=".6"/></svg>
    www.brookhollowfamilydentistry.example
  </div>

  <div class="abs brand">
    <span class="brand-dot"></span>
    <span class="brand-name">Brookhollow<br>Family Dentistry</span>
  </div>
  <p class="abs return-address">4270 Maplecrest Drive, Suite<br>#210 Raleigh, NC 27615</p>
  <div class="abs stamp-box"></div>
  <div class="abs address-line address-line--1"></div>
  <div class="abs address-line address-line--2"></div>
  <div class="abs address-line address-line--3"></div>
</section>

</body>
</html>
```